INSURANCE COMPANY POSTCARD

WE ARE A WELL KNOWN INSURANCE AGENCY WORKING UNDER NEW OWNERSHIP USING THE OLD OWNERS NAME STILL, AS OUR TINY COMMUNITY WOULDN'T BE ABLE TO UNDERSTAND THAT WE ARE THE SAME AS BEFORE, JUST A NEW OWNER. WE PROVIDE AUTO, HOME, COMMERCIAL, FLOOD AND EVENT INSURANCE.

Industry/Entity Type

Insurance

```html
<!DOCTYPE html>
<html lang="en">
<head>
<meta charset="utf-8">
<title>Harlow Insurance Agency Postcard</title>
<link rel="stylesheet" href="https://fonts.googleapis.com/css2?family=Roboto+Condensed:ital,wght@1,700&family=Source+Sans+3:ital,wght@0,400;0,600;1,400;1,700&display=swap">
<style>
  :root {
    --stage: #e7e5e1;
    --panel-grey: #bcbdc1;
    --panel-shade: #9fa0a6;
    --navy: #1d2466;
    --stripe: #2b2a7c;
    --purple: #33287a;
    --sky: #6fb8ea;
    --role-blue: #86b9ea;
    --white: #ffffff;
    --logo-grey: #7c7f88;
  }
  * { margin: 0; padding: 0; box-sizing: border-box; }
  html, body { width: 1200px; height: 1000px; overflow: hidden; }
  body {
    background: var(--stage);
    position: relative;
    font-family: "Source Sans 3", "Helvetica Neue", Arial, sans-serif;
  }

  /* ---------- Front of card ---------- */
  .card-front {
    position: absolute; left: 44px; top: 36px;
    width: 596px; height: 461px;
    background: var(--panel-grey);
    overflow: hidden;
  }
  .edge-shade {
    position: absolute; inset: 0;
    background: linear-gradient(100deg, rgba(0,0,0,0) 55%, rgba(90,92,100,.35) 60%, rgba(0,0,0,0) 62%);
  }
  .media {
    position: absolute; inset: 0;
    background: var(--white);
    clip-path: polygon(318px 0, 596px 0, 596px 461px, 254px 461px);
  }
  .media-grid {
    position: absolute; inset: 0;
    clip-path: polygon(338px 0, 596px 0, 596px 461px, 274px 461px);
  }
  .divider { position: absolute; inset: 0; }
  .front-brand {
    position: absolute; left: 20px; top: 22px; width: 300px;
    text-align: center; color: var(--white); font-weight: 600;
  }
  .front-brand .brand-name { font-size: 48px; line-height: 1; }
  .front-brand .brand-sub { font-size: 24px; line-height: 1.2; }
  .services {
    position: absolute; left: 31px; top: 170px;
    font-family: "Roboto Condensed", "Arial Narrow", sans-serif;
    font-style: italic; font-weight: 700;
    font-size: 36px; line-height: 39px;
    color: var(--navy); text-transform: uppercase;
  }
  .photo { position: absolute; }
  .photo-family {
    left: 290px; top: 0; width: 306px; height: 208px;
    background: linear-gradient(180deg, #5fa6de 0%, #a9cdea 35%, #e9e4dc 60%, #f4f4f4 100%);
  }
  .photo-nurse {
    left: 270px; top: 214px; width: 154px; height: 162px;
    background: linear-gradient(180deg, #eef1f3 0%, #b9d3e6 45%, #4f8fc4 100%);
  }
  .photo-driver {
    left: 429px; top: 214px; width: 167px; height: 162px;
    background: linear-gradient(135deg, #dfe2e6 0%, #a6acb4 45%, #3a3d44 100%);
  }
  .call-bar {
    position: absolute; left: 250px; top: 380px; width: 346px; height: 81px;
    background: var(--navy); color: var(--white);
    padding-left: 36px; text-align: center;
  }
  .call-bar .call-label {
    font-style: italic; font-weight: 700; font-size: 19px;
    color: var(--sky); text-transform: uppercase; margin-top: 6px;
  }
  .call-bar .call-number {
    display: flex; align-items: center; justify-content: center; gap: 8px;
    font-style: italic; font-size: 30px; line-height: 1.1;
  }

  /* ---------- Back of card ---------- */
  .card-back {
    position: absolute; left: 562px; top: 510px;
    width: 595px; height: 460px;
    background: var(--white); overflow: hidden;
  }
  .photo-house {
    left: 0; top: 0; width: 378px; height: 148px;
    background: linear-gradient(90deg, #8a8e80 0%, #a9b3a0 35%, #c7d6e6 65%, #ffffff 100%);
  }
  .photo-house::after {
    content: ""; position: absolute; left: 0; bottom: 0; width: 70%; height: 30px;
    background: linear-gradient(90deg, #4f8a36, rgba(120,170,90,0));
  }
  .back-brand {
    position: absolute; left: 200px; top: 46px; width: 260px;
    text-align: center; color: var(--logo-grey); font-weight: 600;
  }
  .back-brand .brand-name { font-size: 44px; line-height: 1; }
  .back-brand .brand-sub { font-size: 24px; line-height: 1.2; }
  .contact-panel {
    position: absolute; left: 0; top: 148px; width: 288px; height: 232px;
    background: var(--purple); color: var(--white); text-align: center;
    padding-top: 20px;
  }
  .contact-strip {
    position: absolute; left: 0; top: 380px; width: 74px; height: 80px;
    background: var(--purple);
  }
  .staff { margin-bottom: 16px; padding-left: 6px; }
  .staff .name { font-size: 17px; line-height: 1.2; }
  .staff .role { font-size: 11px; color: var(--role-blue); }
  .staff .email { font-size: 12px; line-height: 1.4; }
  .contact-panel .call-label {
    margin-top: 22px; font-style: italic; font-weight: 700; font-size: 11px;
    color: var(--role-blue); text-transform: uppercase;
  }
  .phones {
    display: flex; justify-content: center; gap: 22px;
    font-style: italic; font-size: 15px;
  }
  .phones span { display: inline-flex; align-items: center; gap: 4px; }
</style>
</head>
<body>

<section class="card-front">
  <div class="edge-shade"></div>

  <div class="front-brand">
    <div class="brand-name">Harlow</div>
    <div class="brand-sub">Insurance Agency</div>
  </div>

  <h1 class="services">We provide<br>auto, home,<br>commercial,<br>flood and<br>event<br>insurance.</h1>

  <div class="media">
    <div class="media-grid">
      <div class="photo photo-family" role="img" aria-label="Smiling family of four outdoors under a blue sky"></div>
      <div class="photo photo-nurse" role="img" aria-label="Nurse in blue scrubs with medical staff"></div>
      <div class="photo photo-driver" role="img" aria-label="Happy driver giving a thumbs up from a car"></div>
      <div class="call-bar">
        <p class="call-label">Call us today at</p>
        <p class="call-number">
          <svg width="26" height="26" viewBox="0 0 26 26" aria-hidden="true">
            <circle cx="13" cy="13" r="11.5" fill="none" stroke="var(--sky)" stroke-width="2"/>
            <path d="M9 7.5c-1 .6-1.6 1.6-1.2 3.1.9 3.4 3.6 6.3 7 7.4 1.4.4 2.5-.1 3.2-1l-2.2-2.1-1.6 1c-1.6-.8-2.9-2.2-3.6-3.8l1-1.5z" fill="var(--sky)"/>
          </svg>
          555.214.7300
        </p>
      </div>
    </div>
    <svg class="divider" width="596" height="461" viewBox="0 0 596 461" aria-hidden="true">
      <polygon points="318,0 334,0 270,461 254,461" fill="var(--stripe)"/>
    </svg>
  </div>
</section>

<section class="card-back">
  <div class="photo photo-house" role="img" aria-label="Suburban two-storey house with a green lawn"></div>
  <div class="back-brand">
    <div class="brand-name">Harlow</div>
    <div class="brand-sub">Insurance Agency</div>
  </div>

  <div class="contact-panel">
    <div class="staff">
      <p class="name">Glen Mercer | <span class="role">Owner/Sales/Agent</span></p>
      <p class="email">gmercerins@example.net</p>
    </div>
    <div class="staff">
      <p class="name">Nora Vance | <span class="role">Agent</span></p>
      <p class="email">noravance@example.net</p>
    </div>
    <div class="staff">
      <p class="name">Rita Colby | <span class="role">CSR/Agent</span></p>
      <p class="email">rcolbyins@example.com</p>
    </div>
    <p class="call-label">Call us today at</p>
    <div class="phones">
      <span>
        <svg width="14" height="14" viewBox="0 0 26 26" aria-hidden="true">
          <circle cx="13" cy="13" r="11.5" fill="none" stroke="var(--role-blue)" stroke-width="2.5"/>
          <path d="M9 7.5c-1 .6-1.6 1.6-1.2 3.1.9 3.4 3.6 6.3 7 7.4 1.4.4 2.5-.1 3.2-1l-2.2-2.1-1.6 1c-1.6-.8-2.9-2.2-3.6-3.8l1-1.5z" fill="var(--role-blue)"/>
        </svg>555.214.7300
      </span>
      <span>
        <svg width="14" height="14" viewBox="0 0 14 14" aria-hidden="true">
          <rect x="3" y="1" width="8" height="4" fill="none" stroke="var(--role-blue)" stroke-width="1.3"/>
          <rect x="1" y="5" width="12" height="6" rx="1" fill="none" stroke="var(--role-blue)" stroke-width="1.3"/>
          <rect x="4" y="9" width="6" height="4" fill="var(--role-blue)"/>
        </svg>555-214-7311
      </span>
    </div>
  </div>
  <div class="contact-strip"></div>
</section>

</body>
</html>
```